Sleek, Professional Business Card Design Needed

Business Cards - Logo Attached.

We are a solar consulting company. We are national and want our cards to represent the professional high quality products that we offer.

Industry/Entity Type

Business

Contact Information for Business Card

n/a

Requirements
Must have
• Design
• Name
• Position
• Number
• Email
• Address
Should not have
• Not be too crowded

```html
<!DOCTYPE html>
<html lang="en">
<head>
<meta charset="utf-8">
<title>Sunward Grid – Business Cards</title>
<link href="https://fonts.googleapis.com/css2?family=Didact+Gothic&family=Montserrat:wght@600;700&display=swap" rel="stylesheet">
<style>
  :root {
    --backdrop: #2b2b2d;
    --lime-light: #d3ea5e;
    --lime: #9ccb3b;
    --lime-deep: #8cc13a;
    --blue: #1d95d3;
    --ink: #5a5a5a;
    --paper: #ffffff;
  }
  * { box-sizing: border-box; margin: 0; padding: 0; }
  html, body { width: 1200px; height: 840px; overflow: hidden; }
  body {
    background: var(--backdrop);
    font-family: "Didact Gothic", "Century Gothic", sans-serif;
    position: relative;
  }
  .card {
    position: absolute;
    width: 540px;
    height: 310px;
    border-radius: 22px;
    overflow: hidden;
    box-shadow: 0 18px 40px rgba(0,0,0,0.45);
  }

  /* Front */
  .card-front {
    left: 50px; top: 120px;
    background: linear-gradient(110deg, var(--lime-light) 0%, var(--lime) 45%, var(--lime-deep) 100%);
    color: var(--paper);
    display: flex; flex-direction: column; align-items: center; justify-content: center;
  }
  .front-brand { display: flex; align-items: center; gap: 14px; }
  .brand-dot { width: 34px; height: 34px; border: 4px solid currentColor; border-radius: 50%; }
  .brand-name {
    font-family: "Montserrat", sans-serif; font-weight: 700;
    font-size: 34px; letter-spacing: 1px; text-transform: uppercase;
  }
  .front-rule { width: 250px; height: 2px; background: var(--paper); margin: 12px 0 30px; }
  .front-web { font-size: 15px; letter-spacing: 3px; }

  /* Back */
  .card-back {
    left: 610px; top: 410px;
    background: var(--paper);
  }
  .back-brand {
    position: absolute; left: 34px; top: 58px;
    display: flex; align-items: center; gap: 12px; color: var(--blue);
  }
  .back-brand .brand-name { font-size: 26px; }
  .back-brand .brand-dot { width: 28px; height: 28px; border-width: 3px; }
  .back-rule {
    position: absolute; left: 34px; top: 104px;
    width: 230px; height: 2px; background: var(--lime);
  }
  .contact {
    position: absolute; left: 34px; bottom: 34px;
    list-style: none; color: var(--ink); font-size: 15px; line-height: 22px;
  }
  .contact li { display: flex; align-items: center; gap: 9px; }
  .contact .plain { padding-left: 0; }
  .contact svg { width: 13px; height: 13px; flex: none; }

  .side-band {
    position: absolute; right: 0; top: 0; width: 180px; height: 100%;
    background: var(--lime);
  }
  .side-band .band-top {
    height: 46%; background: var(--blue);
    color: var(--paper); text-align: center; padding-top: 28px;
    font-family: "Montserrat", sans-serif; font-weight: 700; font-size: 16px; line-height: 22px;
    text-transform: uppercase;
  }
  .side-band .band-top .role { font-weight: 600; font-size: 14px; }
  .band-ring {
    position: absolute; right: 20px; top: 92px;
    width: 160px; height: 160px; border-radius: 50%;
    border: 4px solid var(--paper);
  }
</style>
</head>
<body>
  <section class="card card-front">
    <div class="front-brand">
      <span class="brand-dot"></span>
      <span class="brand-name">Sunward Grid</span>
    </div>
    <div class="front-rule"></div>
    <p class="front-web">www.sunwardgrid.com</p>
  </section>

  <section class="card card-back">
    <div class="back-brand">
      <span class="brand-dot"></span>
      <span class="brand-name">Sunward Grid</span>
    </div>
    <div class="back-rule"></div>

    <ul class="contact">
      <li class="plain">412 Cedar Row</li>
      <li class="plain">Juneau, Alaska 99801</li>
      <li>
        <svg viewBox="0 0 16 16" aria-hidden="true"><path fill="#1d95d3" d="M3 1h3l1.5 4-2 1.3a9 9 0 0 0 4.2 4.2L11 8.5l4 1.5v3a2 2 0 0 1-2 2A12 12 0 0 1 1 3a2 2 0 0 1 2-2z"/></svg>
        555 214 0917
      </li>
      <li>
        <svg viewBox="0 0 16 16" aria-hidden="true"><rect x="1" y="3" width="14" height="10" rx="1.5" fill="#1d95d3"/><path d="M1.5 4l6.5 5 6.5-5" fill="none" stroke="#fff" stroke-width="1.3"/></svg>
        hello@sunwardgrid.com
      </li>
      <li>
        <svg viewBox="0 0 16 16" aria-hidden="true"><circle cx="8" cy="8" r="7" fill="#1d95d3"/><path d="M1 8h14M8 1c-3 3.5-3 10.5 0 14M8 1c3 3.5 3 10.5 0 14" fill="none" stroke="#fff" stroke-width="1"/></svg>
        www.sunwardgrid.com
      </li>
    </ul>

    <div class="side-band">
      <div class="band-top">
        <p class="person">Daniel Reyes</p>
        <p class="role">CEO/Founder</p>
      </div>
    </div>
    <div class="band-ring"></div>
  </section>
</body>
</html>
```